Ad Banner for knowledge management portal - Promote Knowledge Submission

This banner is used in knowledge management web site.

1. Banner size: 940x380
2. Business background: Provides maintenance, design and engineering, construction, machinery operation, material procurement and production management services for petrochemical and refinery business
3. We would like to see designs that
- Promote the benefits of sharing "Lesson Learned".
- Use the keyword "I will do it better if I have to do it again"
- Promote employees to submit "Lesson Learned". It is a lesson learned from work, submitted using a predefined form template.
- Promote a campaign that will give out souvenir for all employees who submit "Lesson Learned"
- Has the message "Click here to learn more about Lesson Learned"

Requirements
Must have
• Must have a picture of technician examining machine or equipments (using cartoon character)
Should not have
• Should not include picture of real people in the design

```html
<!DOCTYPE html>
<html lang="en">
<head>
<meta charset="UTF-8">
<title>Lesson Learned Banner</title>
<link rel="stylesheet" href="https://fonts.googleapis.com/css2?family=Oswald:wght@500;600;700&display=swap">
<style>
  :root {
    --page-bg: #ffffff;
    --blue-deep: #1f33c9;
    --blue-mid: #5a6fe0;
    --haze: #e9e6f4;
    --lilac: #c9b7d8;
    --orange: #e8823a;
    --red-hot: #c8321c;
    --band: rgba(8, 8, 10, 0.92);
    --ink: #111111;
    --white: #ffffff;
    --figure-red: #d8261a;
    --figure-dark: #9a140c;
  }
  * { margin: 0; padding: 0; box-sizing: border-box; }
  html, body {
    width: 1200px;
    height: 900px;
    overflow: hidden;
    background: var(--page-bg);
  }
  .banner {
    position: absolute;
    left: 51px;
    top: 214px;
    width: 1107px;
    height: 446px;
    overflow: hidden;
    font-family: "Oswald", "Arial Narrow", sans-serif;
  }
  .banner__scene {
    position: absolute;
    inset: 0;
    background:
      radial-gradient(ellipse 420px 260px at 980px 120px, rgba(255, 180, 70, 0.75), transparent 70%),
      radial-gradient(ellipse 380px 220px at 1000px 380px, rgba(230, 110, 60, 0.7), transparent 70%),
      linear-gradient(100deg, var(--blue-deep) 0%, var(--blue-mid) 22%, var(--haze) 45%, var(--lilac) 62%, var(--orange) 82%, var(--red-hot) 100%);
  }
  .banner__band {
    position: absolute;
    left: 0;
    top: 167px;
    width: 100%;
    height: 114px;
    background: var(--band);
  }
  .banner__mascot {
    position: absolute;
    left: 50px;
    top: 14px;
    width: 300px;
    height: 412px;
    border-radius: 120px 120px 30px 30px;
    background: radial-gradient(ellipse at 40% 30%, var(--figure-red), var(--figure-dark) 80%);
    opacity: 0.9;
  }
  .headline {
    position: absolute;
    left: 370px;
    top: 14px;
    color: var(--ink);
    text-shadow: 0 0 6px rgba(255, 255, 255, 0.9);
    line-height: 1;
  }
  .headline__main {
    display: block;
    font-weight: 600;
    font-size: 60px;
    letter-spacing: 0.5px;
  }
  .headline__sub {
    display: block;
    margin-top: 8px;
    font-weight: 600;
    font-size: 42px;
  }
  .campaign {
    position: absolute;
    top: 207px;
    left: 340px;
    display: flex;
    gap: 60px;
    list-style: none;
    color: var(--white);
    font-weight: 500;
    font-size: 24px;
  }
  .campaign__item {
    display: flex;
    align-items: center;
    gap: 14px;
  }
  .campaign__item--souvenir { margin-left: 0; }
  .campaign__arrow { width: 10px; height: 10px; }
  .cta {
    position: absolute;
    right: 20px;
    bottom: 14px;
    color: var(--white);
    font-weight: 500;
    font-size: 20px;
    text-decoration: none;
    text-shadow: 1px 1px 2px #000, 0 0 3px #000;
  }
</style>
</head>
<body>
  <section class="banner">
    <div class="banner__scene" role="img" aria-label="Backdrop collage of engineering rulers and drafting tools on blue at left, refinery plant pipes glowing orange at right"></div>
    <div class="banner__band"></div>
    <div class="banner__mascot" role="img" aria-label="Red cartoon technician figure holding a large grey wrench"></div>

    <h1 class="headline">
      <span class="headline__main">I will do it better</span>
      <span class="headline__sub">If I have to do it again</span>
    </h1>

    <ul class="campaign">
      <li class="campaign__item">
        <svg class="campaign__arrow" viewBox="0 0 10 10"><path d="M0 4h5V1l5 4-5 4V6H0z" fill="#fff"/></svg>
        Submit "Lesson Learned"
      </li>
      <li class="campaign__item campaign__item--souvenir">
        <svg class="campaign__arrow" viewBox="0 0 10 10"><path d="M0 4h5V1l5 4-5 4V6H0z" fill="#fff"/></svg>
        Souvenir for all who submit
      </li>
    </ul>

    <a class="cta" href="#">Click here to learn more about Lesson Learned</a>
  </section>
</body>
</html>
```